Tarnwell needs a Monthly Newsletter

We need a newsletter design for a company located in Sydney Australia. We are an IT Services and Software Development company with both arms separated as a business. We would like to see designs that follow the same elements that our website has being www.tarnwell-example.com.au.
It needs an element of our corporate blue logo in it and would like the same colour elements included throughout the file.
The file needs to be MailChimp compatible and we would need all the files being HTML, the graphics, the PSD files, the MailChimp ready file, etc.

```html
<!DOCTYPE html>
<html lang="en">
<head>
<meta charset="utf-8">
<title>Tarnwell Monthly Newsletter</title>
<link href="https://fonts.googleapis.com/css2?family=Open+Sans:wght@400;600;700&display=swap" rel="stylesheet">
<style>
:root{
  --brand:#1f73c9;
  --brand-mid:#3585d6;
  --brand-deep:#1b5fb2;
  --band:#1e64b8;
  --footer:#0d4f9c;
  --teal:#17877f;
  --ink:#3a3a3a;
  --muted:#6b6b6b;
  --white:#ffffff;
  --photo-a:#7fb4e4;
  --photo-b:#2a6fb8;
}
*{box-sizing:border-box;margin:0;padding:0}
html,body{width:1200px;height:2384px;overflow:hidden;background:var(--white)}
body{font-family:"Open Sans",Arial,sans-serif;color:var(--ink);position:relative}
.abs{position:absolute}
.header{left:0;top:0;width:1200px;height:240px;background:var(--white)}
.brand{left:140px;top:34px;display:flex;align-items:center;gap:18px}
.brand-dot{width:88px;height:88px;border-radius:50%;background:var(--brand)}
.brand-name{font-size:58px;font-weight:700;color:var(--brand);letter-spacing:1px;line-height:1}
.social-top{left:680px;top:20px;display:flex;gap:12px}
.social-top span{width:88px;height:88px;display:block}
.s1{background:#3b6fc4}.s2{background:#39a9e6}.s3{background:#d9472f}.s4{background:#c4263a}.s5{background:#f08a1c}
.view-online{right:40px;top:128px;font-size:20px;color:var(--muted)}
.hero{left:0;top:240px;width:1200px;height:220px;background:var(--brand);color:var(--white);
  display:flex;align-items:center;justify-content:center;text-align:center;font-size:40px;line-height:60px;font-weight:400}
.col-title{font-size:42px;line-height:54px;font-weight:400;color:var(--ink)}
.col-body{font-size:17px;line-height:24px;color:var(--muted);margin-top:12px}
.feature{left:0;width:1200px;height:416px}
.feature-case{top:732px;background:var(--brand-mid)}
.feature-campaign{top:1148px;background:var(--brand-deep)}
.feature h2{font-size:42px;line-height:54px;font-weight:400;color:var(--white)}
.feature p{font-size:18px;line-height:26px;color:var(--white);margin-top:8px}
.more{display:flex;align-items:center;gap:18px;font-size:38px;color:var(--white)}
.photo{background:linear-gradient(135deg,var(--photo-a),var(--photo-b))}
.btn{height:80px;width:456px;background:var(--teal);color:var(--white);display:flex;align-items:center;justify-content:center;gap:20px;font-size:26px;font-weight:600;letter-spacing:1px}
.action-band{left:0;top:2032px;width:1200px;height:116px;background:var(--band);color:var(--white);font-size:42px}
.action{display:flex;align-items:center;gap:22px;top:26px}
.footer{left:0;top:2148px;width:1200px;height:236px;background:var(--footer);color:var(--white)}
.social-foot{left:100px;top:40px;display:flex;gap:14px}
.social-foot span{width:80px;height:80px;border:3px solid var(--white);display:block}
.copyright{left:100px;top:150px;font-size:18px}
.contact{left:580px;top:24px}
.contact h3{font-size:42px;font-weight:400}
.contact p{font-size:18px;line-height:26px}
</style>
</head>
<body>
<header class="abs header">
  <div class="abs brand"><span class="brand-dot"></span><span class="brand-name">Tarnwell</span></div>
  <div class="abs social-top"><span class="s1"></span><span class="s2"></span><span class="s3"></span><span class="s4"></span><span class="s5"></span></div>
  <div class="abs view-online">If you can't see this email? View it online</div>
</header>

<section class="abs hero">Tarnwell provides highly effective IT solutions<br>and services.</section>

<section class="abs" style="left:100px;top:494px;width:460px">
  <h2 class="col-title">Tip of the month</h2>
  <p class="col-body">Consetetur sadipscing elitr, sed diam nonumy eirmod tempor invidunt ut labore et dolore magna aliquyam erat, sed diam voluptua. At vero eos et accusam et justo duo dolores et ea rebum. Stet clita kasd gubergren, no takimata sanctus est Lorem ipsum dolor sit amet.</p>
</section>
<section class="abs" style="left:604px;top:494px;width:480px">
  <h2 class="col-title">Did you know?</h2>
  <p class="col-body">At vero eos et accusam et justo duo dolores et ea rebum. Stet clita kasd gubergren, no sea takimata sanctus est Lorem ipsum dolor sit amet. Lorem ipsum dolor sit amet, consetetur sadipscing elitr, sed diam nonumy eirmod tempor invidunt ut labore et dolore.</p>
</section>

<section class="abs feature feature-case">
  <div class="abs" style="left:100px;top:44px;width:460px">
    <h2>Case Studies</h2>
    <p>Lorem ipsum dolor sit amet, sed diam nonumy eirmod tempor invidunt ut labore et dolore magna aliquyam erat, sed diam voluptua. At vero eos et accusam et justo duo dolores et ea rebum. Stet clita kasd gubergren, no sea takimata sanctus est Lorem ipsum.</p>
  </div>
  <div class="abs more" style="left:128px;top:312px">More Details
    <svg width="76" height="76" viewBox="0 0 76 76"><circle cx="38" cy="38" r="34" fill="none" stroke="#fff" stroke-width="5"/><path d="M22 38h30M40 26l12 12-12 12" fill="none" stroke="#fff" stroke-width="5" stroke-linecap="round" stroke-linejoin="round"/></svg>
  </div>
  <div class="abs photo" style="left:600px;top:0;width:460px;height:416px" role="img" aria-label="Photo of a hand touching a glowing digital interface"></div>
</section>

<section class="abs feature feature-campaign">
  <div class="abs photo" style="left:100px;top:0;width:460px;height:416px" role="img" aria-label="Photo of hands holding a tablet with technology graphics"></div>
  <div class="abs" style="left:604px;top:32px;width:480px">
    <h2>Campaign this month</h2>
    <p>Lorem ipsum dolor sit amet, sed diam nonumy eirmod tempor invidunt ut labore et dolore magna aliquyam erat, sed diam voluptua. At vero eos et accusam et justo duo dolores et ea rebum. Stet clita kasd gubergren, no sea takimata sanctus est Lorem ipsum.</p>
  </div>
  <div class="abs more" style="left:604px;top:300px">
    <svg width="76" height="76" viewBox="0 0 76 76"><circle cx="38" cy="38" r="34" fill="none" stroke="#fff" stroke-width="5"/><path d="M54 38H24M36 26L24 38l12 12" fill="none" stroke="#fff" stroke-width="5" stroke-linecap="round" stroke-linejoin="round"/></svg>More Details
  </div>
</section>

<section class="abs" style="left:100px;top:1606px;width:460px">
  <h2 class="col-title">New Technologies</h2>
  <p class="col-body">Consetetur sadipscing elitr, sed diam nonumy eirmod tempor invidunt ut labore et dolore magna aliquyam erat, sed diam voluptua. At vero eos et accusam et justo duo dolores et ea rebum. Stet clita kasd gubergren, no takimata sanctus est Lorem ipsum dolor sit amet.</p>
</section>
<section class="abs" style="left:604px;top:1606px;width:480px">
  <h2 class="col-title">News</h2>
  <p class="col-body">At vero eos et accusam et justo duo dolores et ea rebum. Stet clita kasd gubergren, no sea takimata sanctus est Lorem ipsum dolor sit amet. Lorem ipsum dolor sit amet, consetetur sadipscing elitr, sed diam nonumy eirmod tempor invidunt ut labore et dolore.</p>
</section>

<div class="abs btn" style="left:100px;top:1892px">
  <svg width="44" height="44" viewBox="0 0 44 44"><circle cx="22" cy="22" r="19" fill="none" stroke="#fff" stroke-width="3"/><path d="M22 12v18M14 23l8 8 8-8" fill="none" stroke="#fff" stroke-width="3" stroke-linecap="round" stroke-linejoin="round"/></svg>SEE MORE DETAILS</div>
<div class="abs btn" style="left:604px;top:1892px">
  <svg width="44" height="44" viewBox="0 0 44 44"><circle cx="22" cy="22" r="19" fill="none" stroke="#fff" stroke-width="3"/><path d="M22 12v18M14 23l8 8 8-8" fill="none" stroke="#fff" stroke-width="3" stroke-linecap="round" stroke-linejoin="round"/></svg>SEE MORE DETAILS</div>

<section class="abs action-band">
  <div class="abs action" style="left:100px">
    <svg width="56" height="56" viewBox="0 0 56 56"><rect x="6" y="20" width="44" height="12" fill="#fff"/><rect x="10" y="32" width="36" height="20" fill="#fff"/><rect x="25" y="20" width="6" height="32" fill="var(--band)"/><path d="M28 20c-6-10-16-10-14-3 1 3 8 3 14 3zm0 0c6-10 16-10 14-3-1 3-8 3-14 3z" fill="none" stroke="#fff" stroke-width="3"/></svg>
    Help us decide</div>
  <div class="abs action" style="left:576px">
    <svg width="60" height="46" viewBox="0 0 60 46"><rect x="2" y="4" width="56" height="38" fill="#fff"/><path d="M4 6l26 20 26-20" fill="none" stroke="var(--band)" stroke-width="4"/></svg>
    Subscribe Now!</div>
</section>

<footer class="abs footer">
  <div class="abs social-foot"><span></span><span></span><span></span><span></span><span></span></div>
  <div class="abs copyright">© Copyright 2013 - All Rights Reserved</div>
  <div class="abs contact">
    <h3>Contact Us</h3>
    <p>Suite 4, level 2, 41 Harbour Lane<br>Northvale NSW 2199<br>info@tarnwell-example.com.au</p>
  </div>
</footer>
</body>
</html>
```